Meadowlark Behavioral Partners, LLC Needs Modern Business Card Design.

We provide behavioral health services from western Kansas to eastern Kansas. There is an abundance of competition for the services we provide with our main competitor being larger and having significantly more financial resources; however, the quality of services we provide is greater and we have started to catch the attention of the State of Kansas. We had a great logo designed by PixelGuild - this will be used to build upon our brand. The logo (attached) should be used in the card development. We want something unique, modern, but also a card design that clearly states our name, contact info, provides the name and unqiue location of each clinician, etc. Rounded edges, or a unique size, just something that makes our business card stand out from others. I have also uploaded each clinician's name and their unique location and phone number.

Our idea is to have one side be black with our logo. Then, on the other side have business cards for each individual. Plus, we want one card that is "generic" with no specific clinician's name listed so that we can give clients an appointment card when they leave. Some clinicians have two locations - we're open to design and background color, but we have started going with branding colors of black, the yellow in the logo files attached, and sometimes a gray. Our new office has been decorated using this theme.

Target Market(s)

individuals and families in need of behavioral health services; potential professional referral sources; existing referral sources

Industry/Entity Type

Business

Contact Information for Business Card

I attached a Word doc that provides clinician names, credentials and location information specific to each individual.

Font styles to use
Serif

Colors
000000
fbed22
dbdbdb
9d9d9d
c3c3c3

Requirements
Must have
• 1) use of the company logo that has been attached; 2) a template that provides us space to individualize business cards for all of our clinicians; 3) should stick to the colors we are branding with: black, yellow from the logo file, maybe a gray shade and we're open to a suggestion on a shade of white.
Nice to have
• Group discussion culminated in the thought that one side would be black with just our logo - no clinician names, etc. A unique design - rounded edges, unique size, some catchy lay-out would be nice.
Should not have
• Must not be too busy. Should look "clean." The project should stick to branding colors: black, yellow (from the logo file), maybe a gray and shade of white.

```html
<!DOCTYPE html>
<html lang="en">
<head>
<meta charset="utf-8">
<title>Meadowlark Behavioral Partners – Business Cards</title>
<link href="https://fonts.googleapis.com/css2?family=EB+Garamond:ital,wght@0,400;0,500;1,400&family=Roboto:wght@700&display=swap" rel="stylesheet">
<style>
  :root {
    --bg: #ececec;
    --card-dark: #262626;
    --card-light: #ffffff;
    --brand-yellow: #f5b800;
    --ink: #2b2b2b;
    --ink-soft: #555555;
    --rule: #c3c3c3;
    --label: #2a2a2a;
  }
  * { box-sizing: border-box; margin: 0; padding: 0; }
  html, body { width: 1200px; height: 789px; overflow: hidden; }
  body {
    background: var(--bg);
    font-family: "EB Garamond", Georgia, serif;
    color: var(--ink);
    position: relative;
  }
  .card {
    position: absolute;
    width: 427px;
    height: 244px;
    border-radius: 10px;
    box-shadow: 0 6px 8px rgba(0,0,0,0.22);
  }
  .card--front { left: 139px; top: 106px; background: var(--card-dark); }
  .card--back { left: 634px; top: 106px; background: var(--card-light); }
  .card--appointment { left: 386px; top: 438px; background: var(--card-light); }

  .view-label {
    position: absolute;
    font-family: "Roboto", Arial, sans-serif;
    font-weight: 700;
    font-size: 14px;
    color: var(--label);
    text-align: center;
    width: 427px;
  }
  .view-label--front { left: 139px; top: 371px; }
  .view-label--back { left: 634px; top: 371px; }
  .view-label--appointment { left: 386px; top: 704px; }

  /* Front */
  .brand {
    position: absolute; left: 0; right: 0; top: 108px;
    text-align: center; color: var(--brand-yellow); font-weight: 500;
  }
  .brand__dot {
    display: block; width: 30px; height: 30px; margin: 0 auto 14px;
    border-radius: 50%; background: var(--brand-yellow);
  }
  .brand__name { font-size: 17px; letter-spacing: 1.5px; line-height: 1; }
  .brand__sub { font-size: 9px; letter-spacing: 1.1px; margin-top: 3px; }
  .tagline {
    position: absolute; left: 0; right: 0; top: 197px;
    text-align: center; color: #f2f2f2; font-size: 10px;
  }

  /* Back */
  .person { position: absolute; left: 0; right: 0; top: 98px; text-align: center; }
  .person__name { font-size: 12.5px; color: var(--ink); }
  .person__title { font-size: 11px; font-style: italic; color: var(--ink-soft); margin-top: 1px; }
  .person__email { font-size: 9.5px; color: var(--ink-soft); margin-top: 1px; }

  .contact { position: absolute; font-size: 8px; line-height: 11px; color: var(--ink-soft); }
  .contact--left { left: 23px; top: 200px; }
  .contact--right { right: 23px; top: 200px; text-align: right; }
  .contact__row { display: flex; align-items: center; gap: 3px; }
  .contact--right .contact__row { justify-content: flex-end; }
  .contact__indent { padding-left: 10px; }
  .icon { width: 7px; height: 8px; fill: var(--ink); flex: none; }
  .ord { font-size: 5px; vertical-align: super; line-height: 0; }

  /* Appointment */
  .appointment { position: absolute; left: 114px; width: 199px; top: 77px; text-align: center; font-size: 9.5px; color: var(--ink-soft); }
  .appointment__line { display: block; height: 1px; background: var(--rule); margin: 12px 0 10px; }
  .appointment__line--last { margin-top: 24px; }
  .locations { position: absolute; top: 186px; left: 24px; right: 0; display: flex; }
  .locations .contact { position: static; width: 146px; line-height: 12px; }
  .locations .contact__indent { margin-top: 3px; }
</style>
</head>
<body>
<svg width="0" height="0" style="position:absolute" aria-hidden="true">
  <defs>
    <symbol id="icon-pin" viewBox="0 0 10 14"><path d="M5 0a5 5 0 0 0-5 5c0 3.6 5 9 5 9s5-5.4 5-9a5 5 0 0 0-5-5zm0 7a2 2 0 1 1 0-4 2 2 0 0 1 0 4z"/></symbol>
    <symbol id="icon-phone" viewBox="0 0 14 14"><path d="M3 0.5l2.3 2.7-1.2 1.8c.9 2 2.6 3.6 4.6 4.6l1.8-1.2 2.7 2.3-1.3 2.6C6.3 13.3 .7 7.7.4 1.8z"/></symbol>
  </defs>
</svg>

<section class="card card--front" aria-label="Card front">
  <div class="brand">
    <span class="brand__dot"></span>
    <div class="brand__name">MEADOWLARK</div>
    <div class="brand__sub">BEHAVIORAL PARTNERS, LLC</div>
  </div>
  <p class="tagline">“brighter days ahead”</p>
</section>
<div class="view-label view-label--front">Front</div>

<section class="card card--back" aria-label="Card back">
  <div class="person">
    <div class="person__name">Daniel R. Hollis, LP</div>
    <div class="person__title">President</div>
    <div class="person__email">dhollis@meadowlarkbehavioral.com</div>
  </div>
  <div class="contact contact--left">
    <div class="contact__row"><svg class="icon"><use href="#icon-pin"/></svg><span>418 N. Elm St. Salina Kansas 67401</span></div>
    <div class="contact__row"><svg class="icon"><use href="#icon-phone"/></svg><span>(785) 555-0142</span></div>
  </div>
  <div class="contact contact--right">
    <div class="contact__row"><svg class="icon"><use href="#icon-pin"/></svg><span>207 W. 12<span class="ord">th</span> St., Ste. 104 Emporia, Kansas 66801</span></div>
    <div class="contact__row"><svg class="icon"><use href="#icon-phone"/></svg><span>(844) 555-0186</span></div>
  </div>
</section>
<div class="view-label view-label--back">Back</div>

<section class="card card--appointment" aria-label="Appointment card">
  <div class="appointment">
    <p>Your next appointment with</p>
    <span class="appointment__line"></span>
    <p>has been scheduled for</p>
    <span class="appointment__line appointment__line--last"></span>
  </div>
  <div class="locations">
    <div class="contact">
      <div class="contact__row"><svg class="icon"><use href="#icon-pin"/></svg><span>418 N. Elm St. Salina</span></div>
      <div class="contact__indent">Kansas 67401</div>
      <div class="contact__row"><svg class="icon"><use href="#icon-phone"/></svg><span>(785) 555-0142</span></div>
    </div>
    <div class="contact">
      <div class="contact__row"><svg class="icon"><use href="#icon-pin"/></svg><span>207 W. 12<span class="ord">th</span> St., Ste. 104</span></div>
      <div class="contact__indent">Emporia, Kansas 66801</div>
      <div class="contact__row"><svg class="icon"><use href="#icon-phone"/></svg><span>(844) 555-0186</span></div>
    </div>
    <div class="contact">
      <div class="contact__row"><svg class="icon"><use href="#icon-pin"/></svg><span>245 W. 3<span class="ord">rd</span> Ave. Hays</span></div>
      <div class="contact__indent">Kansas 67601</div>
      <div class="contact__row"><svg class="icon"><use href="#icon-phone"/></svg><span>(785) 555-0173</span></div>
    </div>
  </div>
</section>
<div class="view-label view-label--appointment">For Appointments</div>
</body>
</html>
```